Business Card Design for a Design/Build Firm

Kestrel Forge Partners, Inc. is a firm providing construction professional project management and architectural design services to an international clientele. Contemporary. "Green" movement aware. Business card to have back design/logo. Cards will be on high gloss paper

Target Market(s)

Building Developers and Owners

Industry/Entity Type

Construction

Requirements
Nice to have
• We really would like to use the acronym "KFP" as main focal point fo card design. Company will be known as KFP.
Should not have
• No globes or abstract images of buildings.

```html
<!DOCTYPE html>
<html lang="en">
<head>
<meta charset="utf-8">
<title>KFP Business Card</title>
<link href="https://fonts.googleapis.com/css2?family=Arimo:wght@400;700&display=swap" rel="stylesheet">
<style>
  :root {
    --stage: #3a3a3a;
    --card-black: #0c0c0c;
    --card-grey: #7b7b7b;
    --mark-grey: #8c8c8c;
    --lime: #8dc63f;
    --white: #ffffff;
  }
  html, body {
    margin: 0;
    width: 1067px;
    height: 1200px;
    overflow: hidden;
    background: var(--stage);
    font-family: "Arimo", Arial, sans-serif;
  }
  .sheet {
    position: relative;
    width: 1067px;
    height: 1200px;
  }
  .card {
    position: absolute;
    left: 133px;
    width: 800px;
    height: 457px;
    overflow: hidden;
    box-shadow: 0 12px 30px rgba(0,0,0,0.45);
  }
  .card--front { top: 90px; background: var(--card-black); }
  .card--back  { top: 650px; background: var(--card-grey); }

  .front-texture {
    position: absolute;
    inset: 0;
    background: linear-gradient(135deg, #141414, #070707);
  }
  .front-brand {
    position: absolute;
    left: 0; right: 0;
    top: 150px;
    text-align: center;
    color: var(--mark-grey);
  }
  .brand-mark {
    display: inline-flex;
    align-items: center;
    gap: 14px;
  }
  .brand-square {
    width: 22px;
    height: 22px;
    background: var(--lime);
  }
  .brand-acronym {
    font-weight: 700;
    font-size: 110px;
    line-height: 1;
    letter-spacing: 2px;
  }
  .brand-name {
    font-size: 22px;
    letter-spacing: 1px;
    margin-top: 6px;
    text-transform: uppercase;
  }

  .back-brand {
    position: absolute;
    left: 50px;
    top: 90px;
    color: var(--white);
  }
  .back-brand .brand-acronym { font-size: 80px; }
  .back-brand .brand-name { font-size: 16px; }
  .person {
    position: absolute;
    right: 60px;
    top: 42px;
    text-align: right;
  }
  .person-name {
    color: var(--lime);
    font-size: 26px;
    margin: 0;
    font-weight: 400;
  }
  .person-role {
    color: var(--white);
    font-size: 14px;
    margin: 2px 0 0;
  }
  .contact {
    position: absolute;
    left: 50px;
    top: 245px;
    list-style: none;
    margin: 0;
    padding: 0;
    color: var(--white);
    font-size: 16px;
  }
  .contact li {
    display: flex;
    align-items: center;
    gap: 10px;
    margin-bottom: 8px;
  }
  .contact .phone { font-size: 20px; }
  .contact svg { width: 16px; height: 16px; fill: var(--white); flex: none; }
  .accent-band {
    position: absolute;
    left: 0;
    bottom: 0;
    width: 800px;
    height: 160px;
  }
</style>
</head>
<body>
<main class="sheet">
  <section class="card card--front" aria-label="Card front">
    <div class="front-texture" role="img" aria-label="Faint repeating brand pattern across the black card face"></div>
    <div class="front-brand">
      <div class="brand-mark">
        <span class="brand-square"></span>
        <span class="brand-acronym">KFP</span>
      </div>
      <div class="brand-name">Kestrel Forge Partners</div>
    </div>
  </section>

  <section class="card card--back" aria-label="Card back">
    <div class="person">
      <h1 class="person-name">Dana Whitfield</h1>
      <p class="person-role">Manager</p>
    </div>

    <div class="back-brand">
      <div class="brand-mark">
        <span class="brand-square"></span>
        <span class="brand-acronym">KFP</span>
      </div>
      <div class="brand-name">Kestrel Forge Partners</div>
    </div>

    <ul class="contact">
      <li>
        <svg viewBox="0 0 16 16" aria-hidden="true"><path d="M8 1 1 7h2v8h4v-5h2v5h4V7h2z"/></svg>
        4821 Alder Crest Road, Brookfield, FL 30000
      </li>
      <li class="phone">
        <svg viewBox="0 0 16 16" aria-hidden="true"><rect x="4" y="1" width="8" height="14" rx="1.5"/><rect x="5.5" y="3" width="5" height="8" fill="#7b7b7b"/></svg>
        400 555 0182
      </li>
      <li>
        <svg viewBox="0 0 16 16" aria-hidden="true"><path d="M1 4h14v9H1z"/><path d="M1 4l7 5 7-5" fill="none" stroke="#7b7b7b" stroke-width="1.4"/></svg>
        hello@kestrelforgepartners.com
      </li>
      <li>
        <svg viewBox="0 0 16 16" aria-hidden="true"><circle cx="8" cy="8" r="7"/><path d="M1 8h14M8 1v14M3 4h10M3 12h10" stroke="#7b7b7b" stroke-width="1" fill="none"/></svg>
        www.kestrelforgepartners.com
      </li>
    </ul>

    <svg class="accent-band" viewBox="0 0 800 160" preserveAspectRatio="none" aria-hidden="true">
      <polygon points="0,160 0,140 800,40 800,160" fill="var(--lime)"/>
      <polygon points="0,140 800,40 800,58 0,156" fill="#a4d65e"/>
    </svg>
  </section>
</main>
</body>
</html>
```